CoverLantern.com website re-design - modern engaging website creation

We have an existing website. Www.CoverLantern.com - the content on the site and our widgets are custom built. But the layout and design of our site we just put there as we built the functionality around it. We want a new, bold, and modern design aimed at getting visitors to run a life insurance quote and ultimately apply. Our demographic is centered around those between the ages of 30-60. So we are looking at a complete site overhaul with better pictures, buttons, and an extremely modern design.

Target Market(s)

30-50 year olds

Industry/Entity Type

Life insurance

Coding

Coded - Design and coding required

Number of Pages Required

5+ page

Font styles to use
Other font styles liked:
• Rubik

Colors
0054AA
0677BA
7BADD7
CADEEF
E8F1F8
00AB8E
00BBA5
67D7C9
C6EFE9
E9F9F6
59FF00
82FF00
B8FF75
E3FFCB
F4FFEA

Requirements
Must have
• Matching color schemes from existing website. We have custom widgets on our site now and those must be . White space is important to make it simple for the user to navigate
Nice to have
• Same content - different more modern design
Should not have
• Colors outside of our current color scheme. Should NOT be too similar to our existing site.

```html
<!DOCTYPE html>
<html lang="en">
<head>
<meta charset="utf-8">
<title>CoverLantern – Life Insurance Made Easy</title>
<link rel="stylesheet" href="https://fonts.googleapis.com/css2?family=Rubik:wght@400;500;600;700&display=swap">
<style>
:root{
  --blue:#0054AA;
  --blue-mid:#0677BA;
  --blue-soft:#7BADD7;
  --blue-pale:#E8F1F8;
  --teal:#00AB8E;
  --teal-soft:#C6EFE9;
  --lime:#59FF00;
  --lime-soft:#B8FF75;
  --navy:#0A3F86;
  --ink:#2B2F38;
  --muted:#5a6170;
  --white:#ffffff;
}
*{box-sizing:border-box;margin:0;padding:0}
html,body{width:1200px;height:5277px;overflow:hidden}
body{font-family:"Rubik",sans-serif;color:var(--ink);background:var(--white);position:relative}
.abs{position:absolute}
ul{list-style:none}
a{color:inherit;text-decoration:none}

/* buttons */
.btn{display:inline-flex;align-items:center;gap:10px;background:var(--blue);color:var(--white);font-size:12px;font-weight:600;letter-spacing:.4px;text-transform:uppercase;padding:0 22px;height:38px;border-radius:19px}
.btn svg{width:18px;height:10px}
.btn-outline{background:var(--white);color:var(--blue);border:2px solid var(--blue-soft)}

/* headings */
.section-title{font-size:28px;font-weight:500;color:var(--blue);line-height:1.2}
.section-title em{font-style:normal;color:var(--teal)}
.center-title{font-size:32px;font-weight:600;color:var(--blue);text-align:center;width:1200px;left:0}
.center-title .brand{font-weight:400}

/* tick list */
.ticks li{position:relative;padding-left:30px;font-size:13.5px;line-height:1.7;color:var(--muted);margin-bottom:10px}
.ticks li::before{content:"";position:absolute;left:0;top:3px;width:19px;height:19px;border-radius:50%;background:var(--teal)}
.ticks li::after{content:"";position:absolute;left:6px;top:7px;width:7px;height:4px;border-left:2px solid #fff;border-bottom:2px solid #fff;transform:rotate(-45deg)}

/* nav */
.nav{top:0;left:0;width:1200px;height:92px;z-index:3}
.nav .brand{left:60px;top:28px;font-size:30px;color:var(--blue-mid);font-weight:400}
.nav-links{left:355px;top:38px;display:flex;gap:44px;font-size:12px;color:var(--ink)}
.nav .login{left:993px;top:38px;font-size:12px}
.nav .signup{left:1049px;top:27px;height:36px;padding:0 22px;font-size:11px}

/* hero */
.hero-photo{top:0;left:0;width:1200px;height:600px;background:linear-gradient(100deg,#f6efe6 0%,#efe3cf 35%,#c9a77c 60%,#8a6a48 85%,#6b5238 100%)}
.hero-wave{top:540px;left:0;width:1200px;height:70px}
.hero-title{left:60px;top:196px;font-size:62px;font-weight:700;color:var(--blue);line-height:1.15}
.hero-title em{font-style:normal;color:var(--teal)}
.hero-sub{left:60px;top:362px;font-size:14px;color:var(--ink)}
.hero-cta{left:60px;top:410px}

/* carriers */
.carrier-strip{left:60px;top:584px;width:1080px;height:108px;background:#fff;box-shadow:0 6px 24px rgba(0,40,90,.12);display:flex;justify-content:space-around;align-items:center;font-size:19px;font-weight:500;color:var(--blue)}

/* carrier chips */
.chip{background:#fff;border:2px solid var(--lime-soft);font-size:15px;font-weight:500;color:var(--blue);display:flex;align-items:center;justify-content:center;box-shadow:0 4px 12px rgba(0,40,90,.08)}

/* bands */
.band{left:0;width:1200px}
.photo{role:img}

/* footer */
.footer{top:4843px;left:0;width:1200px;height:434px;background:var(--blue);color:#fff}
.footer h4{font-size:15px;font-weight:500;color:var(--lime);margin-bottom:14px}
.footer li{font-size:11.5px;line-height:22px;color:#e3ecf7}
.footer li::before{content:"- "}
.contact-list li::before{content:""}
.contact-list b{color:var(--lime);font-weight:500}
.contact-list strong{font-weight:600;color:#fff}
</style>
</head>
<body>

<!-- Hero -->
<div class="abs hero-photo" role="img" aria-label="Photo of a smiling father lifting his young daughter in a golden field"></div>
<svg class="abs hero-wave" viewBox="0 0 1200 70" preserveAspectRatio="none"><path d="M0 30 C300 70 700 75 1200 10 L1200 70 L0 70 Z" fill="#fff"/></svg>

<header class="abs nav">
  <div class="abs brand">CoverLantern</div>
  <nav class="abs nav-links"><a>Free Quote</a><a>No Exam</a><a>Articles</a><a>FAQ's</a><a>About</a><a>Contact</a></nav>
  <a class="abs login">LOGIN</a>
  <a class="abs btn signup">SIGN UP</a>
</header>

<h1 class="abs hero-title">Life Insurance<br>Made <em>Easy</em></h1>
<p class="abs hero-sub">Best rates for Term Life Insurance from America's top rated carriers</p>
<a class="abs btn hero-cta">GET A QUOTE <svg viewBox="0 0 18 10"><path d="M0 5h16M12 1l4 4-4 4" stroke="#fff" stroke-width="1.6" fill="none"/></svg></a>

<div class="abs carrier-strip">
  <span>Northvale</span><span>Harbor Mutual</span><span>Crestline Life</span><span>Guardline</span><span>Ridgeway</span><span>Summit Trust</span>
</div>

<!-- Why choose -->
<h2 class="abs center-title" style="top:776px">Why Choose <span class="brand">CoverLantern</span></h2>

<section>
  <h3 class="abs section-title" style="left:60px;top:942px">Life Insurance <em>Online</em></h3>
  <ol class="abs" style="left:60px;top:1000px;list-style:none;font-size:13.5px;color:var(--muted)">
    <li style="display:flex;align-items:center;gap:14px;height:45px"><span style="width:28px;height:28px;border-radius:50%;background:var(--teal);color:#fff;font-size:12px;display:flex;align-items:center;justify-content:center">1.</span>Compare quotes from America's top insurance carriers</li>
    <li style="display:flex;align-items:center;gap:14px;height:45px"><span style="width:28px;height:28px;border-radius:50%;background:var(--teal);color:#fff;font-size:12px;display:flex;align-items:center;justify-content:center">2.</span>Pick your policy</li>
    <li style="display:flex;align-items:center;gap:14px;height:45px"><span style="width:28px;height:28px;border-radius:50%;background:var(--teal);color:#fff;font-size:12px;display:flex;align-items:center;justify-content:center">3.</span>Apply in minutes</li>
  </ol>
  <a class="abs btn" style="left:60px;top:1152px">GET YOUR QUOTE <svg viewBox="0 0 18 10"><path d="M0 5h16M12 1l4 4-4 4" stroke="#fff" stroke-width="1.6" fill="none"/></svg></a>

  <div class="abs" role="img" aria-label="Photo of a father and daughter smiling at a laptop" style="left:672px;top:858px;width:384px;height:424px;border-radius:200px 200px 0 0;border:6px solid #fff;box-shadow:0 6px 20px rgba(0,40,90,.15);background:linear-gradient(160deg,#e9e4dc,#c9b9a3 55%,#7d6a57)"></div>
  <div class="abs chip" style="left:584px;top:952px;width:112px;height:72px">Guardline</div>
  <div class="abs chip" style="left:1028px;top:955px;width:112px;height:70px">Summit Trust</div>
  <div class="abs chip" style="left:597px;top:1046px;width:130px;height:70px">Northvale</div>
  <div class="abs chip" style="left:1000px;top:1046px;width:126px;height:70px;font-size:13px">Harbor Mutual</div>
  <div class="abs chip" style="left:584px;top:1134px;width:110px;height:70px;font-size:13px">Crestline Life</div>
  <div class="abs chip" style="left:1044px;top:1134px;width:86px;height:70px">Ridgeway</div>
</section>

<!-- Compare and Save -->
<svg class="abs band" style="top:1320px;height:540px" viewBox="0 0 1200 540" preserveAspectRatio="none"><path d="M0 40 C250 -10 500 90 800 40 C1000 5 1100 30 1200 10 L1200 500 C900 470 600 560 300 510 C150 490 60 520 0 520 Z" fill="#E8F1F8"/></svg>
<svg class="abs" style="left:450px;top:1708px" width="150" height="150"><circle cx="75" cy="75" r="72" fill="#59FF00"/></svg>
<div class="abs" role="img" aria-label="Photo of a couple smiling while browsing on a tablet" style="left:152px;top:1390px;width:372px;height:414px;border-radius:0 200px 0 0;border:6px solid #fff;box-shadow:0 6px 20px rgba(0,40,90,.15);background:linear-gradient(150deg,#f1ece5,#d8c4ae 55%,#8b7560)"></div>

<div class="abs" style="left:60px;top:1570px;width:190px;display:flex;flex-direction:column;gap:6px">
  <div style="display:flex;background:#fff;border:2px solid var(--lime-soft);height:70px"><div style="width:88px;display:flex;align-items:center;justify-content:center;font-size:13px;font-weight:500;color:var(--blue)">Northvale</div><div style="flex:1;border-left:1px solid #e3e8ef;font-size:6.5px;color:var(--muted);padding:7px 6px;line-height:1.4">$1,000,000 Death Benefit<br>20 Year Level Term<div style="font-size:20px;font-weight:700;color:var(--ink);margin-top:3px">$18<span style="font-size:8px">/mo</span></div></div></div>
  <div style="display:flex;background:#fff;border:2px solid var(--lime-soft);height:70px"><div style="width:88px;display:flex;align-items:center;justify-content:center;font-size:13px;font-weight:500;color:var(--blue)">Guardline</div><div style="flex:1;border-left:1px solid #e3e8ef;font-size:6.5px;color:var(--muted);padding:7px 6px;line-height:1.4">$1,000,000 Death Benefit<br>20 Year Level Term<div style="font-size:20px;font-weight:700;color:var(--ink);margin-top:3px">$21<span style="font-size:8px">/mo</span></div></div></div>
  <div style="display:flex;background:#fff;border:2px solid var(--lime-soft);height:70px"><div style="width:88px;display:flex;align-items:center;justify-content:center;font-size:13px;font-weight:500;color:var(--blue)">Ridgeway</div><div style="flex:1;border-left:1px solid #e3e8ef;font-size:6.5px;color:var(--muted);padding:7px 6px;line-height:1.4">$1,000,000 Death Benefit<br>20 Year Level Term<div style="font-size:20px;font-weight:700;color:var(--ink);margin-top:3px">$23<span style="font-size:8px">/mo</span></div></div></div>
</div>

<h3 class="abs section-title" style="left:674px;top:1476px">Compare and <em>Save</em></h3>
<ul class="abs ticks" style="left:674px;top:1532px;width:470px">
  <li>Get Quotes without having to enter your contact information.</li>
  <li>Decide what's best for you without having to deal with pushy insurance agents.</li>
  <li>Virtual agent tools are available to help you choose what life insurance policy is best for you and your family.</li>
</ul>
<a class="abs btn" style="left:674px;top:1695px">COMPARE CARRIERS <svg viewBox="0 0 18 10"><path d="M0 5h16M12 1l4 4-4 4" stroke="#fff" stroke-width="1.6" fill="none"/></svg></a>

<!-- Virtual Agent -->
<h3 class="abs section-title" style="left:60px;top:1975px">Virtual <em>Agent</em></h3>
<ul class="abs ticks" style="left:60px;top:2032px;width:470px">
  <li>Our Virtual Agent Lumi can help you calculate how much death benefit you need.</li>
  <li>Lumi can help you figure out what type of Life Insurance is right for you and your family.</li>
  <li>Lumi can evaluate your health history and provide you with accurate quotes.</li>
</ul>
<a class="abs btn" style="left:60px;top:2214px">VIRTUAL AGENT <svg viewBox="0 0 18 10"><path d="M0 5h16M12 1l4 4-4 4" stroke="#fff" stroke-width="1.6" fill="none"/></svg></a>
<div class="abs" role="img" aria-label="Illustration of a virtual assistant on a smartphone screen with chat and help icons" style="left:665px;top:1915px;width:420px;height:392px;border-radius:200px 0 0 200px;border:6px solid #fff;box-shadow:0 6px 20px rgba(0,40,90,.15);background:linear-gradient(140deg,#3d4450,#22262d 60%,#0677BA)"></div>

<!-- Live Agent -->
<svg class="abs band" style="top:2385px;height:510px" viewBox="0 0 1200 510" preserveAspectRatio="none"><path d="M0 30 C300 70 600 -10 900 30 C1050 50 1130 20 1200 20 L1200 450 C900 520 500 430 200 480 C100 495 40 500 0 505 Z" fill="#E8F1F8"/></svg>
<svg class="abs" style="left:60px;top:2690px" width="150" height="150"><circle cx="75" cy="75" r="72" fill="#59FF00"/></svg>
<div class="abs" role="img" aria-label="Photo of a smiling call center agent wearing a headset" style="left:72px;top:2416px;width:412px;height:412px;border-radius:50%;border:6px solid #fff;box-shadow:0 6px 20px rgba(0,40,90,.15);background:radial-gradient(circle at 50% 40%,#f5f4f2,#ddd8d2 60%,#b4aca3)"></div>
<div class="abs" style="left:240px;top:2738px;width:310px;height:44px;background:#fff;border:2px solid var(--blue-soft);border-radius:22px;display:flex;align-items:center;gap:10px;padding-left:6px;font-size:14px">
  <span style="width:30px;height:30px;border-radius:50%;background:var(--teal);display:flex;align-items:center;justify-content:center"><svg width="14" height="14" viewBox="0 0 24 24"><path d="M6.6 10.8a15 15 0 006.6 6.6l2.2-2.2c.3-.3.7-.4 1-.2 1.1.4 2.3.6 3.6.6.6 0 1 .4 1 1V20c0 .6-.4 1-1 1A17 17 0 013 4c0-.6.4-1 1-1h3.5c.6 0 1 .4 1 1 0 1.3.2 2.5.6 3.6.1.3 0 .7-.2 1z" fill="#fff"/></svg></span>
  Toll Free: <b style="color:var(--blue);font-weight:600">1-888-555-0142</b>
</div>

<h3 class="abs section-title" style="left:674px;top:2497px">Live Agent <em>Support</em></h3>
<ul class="abs ticks" style="left:674px;top:2554px;width:470px">
  <li>If you need a Live Agent, CoverLantern has you covered. Our CoverLantern Agents are not paid a commission. So if you have questions our agents have the answers that best suit your needs.</li>
</ul>
<div class="abs" style="left:674px;top:2660px;display:flex;align-items:center;gap:10px;font-size:13.5px;color:var(--muted)">
  <span style="width:19px;height:19px;border-radius:50%;background:var(--teal);display:flex;align-items:center;justify-content:center"><svg width="11" height="9" viewBox="0 0 11 9"><rect x=".5" y=".5" width="10" height="8" fill="none" stroke="#fff"/><path d="M.5 .5l5 4 5-4" fill="none" stroke="#fff"/></svg></span>
  Email: <b style="color:var(--blue);font-weight:500">Info@CoverLantern.com</b>
</div>
<a class="abs btn" style="left:674px;top:2716px">LIVE AGENT SUPPORT <svg viewBox="0 0 18 10"><path d="M0 5h16M12 1l4 4-4 4" stroke="#fff" stroke-width="1.6" fill="none"/></svg></a>

<!-- Apply Online -->
<h3 class="abs section-title" style="left:60px;top:3044px">Apply <em>Online</em></h3>
<ul class="abs ticks" style="left:60px;top:3102px;width:480px">
  <li>Pick your policy and apply online in minutes.</li>
  <li>Secure Online Portal keeps your information safe and secure.</li>
  <li>24/7 access to your policy documents.</li>
</ul>
<a class="abs btn" style="left:60px;top:3224px">PORTAL LOGIN <svg viewBox="0 0 18 10"><path d="M0 5h16M12 1l4 4-4 4" stroke="#fff" stroke-width="1.6" fill="none"/></svg></a>
<div class="abs" style="left:694px;top:3236px;width:110px;height:124px;background:var(--lime)"></div>
<div class="abs" role="img" aria-label="Photo of a mother and baby looking at a laptop together" style="left:692px;top:2950px;width:370px;height:410px;border-radius:0 200px 0 0;border:6px solid #fff;box-shadow:0 6px 20px rgba(0,40,90,.15);background:linear-gradient(150deg,#e4e2df,#bfb2a3 55%,#6e5c4c)"></div>
<div class="abs" style="left:652px;top:3112px;width:86px;height:86px;border-radius:50%;background:#fff;border:3px solid var(--teal-soft)"></div>
<a class="abs btn btn-outline" style="left:983px;top:3297px;height:42px;padding:0 26px">APPLY NOW</a>

<!-- Testimonials -->
<svg class="abs band" style="top:3360px;height:660px" viewBox="0 0 1200 660" preserveAspectRatio="none"><path d="M0 60 C200 10 400 110 650 60 C900 10 1050 70 1200 40 L1200 660 L0 660 Z" fill="#E8F1F8"/></svg>
<h2 class="abs center-title" style="top:3594px">What Clients Say About <span class="brand">CoverLantern</span></h2>

<div class="abs" style="left:61px;top:3697px;width:346px;height:216px;background:#fff;padding:44px 28px 0"><div class="abs" style="left:28px;top:-20px;width:44px;height:44px;border-radius:50%;background:var(--blue);color:#fff;font-size:30px;font-weight:700;text-align:center;line-height:52px">“</div><p style="font-size:13.5px;font-weight:500;line-height:1.9">Lorem ipsum dolor sit amet, conteuer adipiscing elit, sed diam nonummy nibh euismod tincidunt ut laoreet dolore magna aliquam erat volutpat.</p><p style="font-size:11.5px;color:var(--muted);margin-top:26px">Dana Reyes, Lorem Ipsum</p></div>
<div class="abs" style="left:428px;top:3697px;width:345px;height:216px;background:#fff;padding:44px 28px 0"><div class="abs" style="left:28px;top:-20px;width:44px;height:44px;border-radius:50%;background:var(--blue);color:#fff;font-size:30px;font-weight:700;text-align:center;line-height:52px">“</div><p style="font-size:13.5px;font-weight:500;line-height:1.9">Lorem ipsum dolor sit amet, conteuer adipiscing elit, sed diam nonummy nibh euismod tincidunt ut laoreet dolore magna aliquam erat volutpat.</p><p style="font-size:11.5px;color:var(--muted);margin-top:26px">Dana Reyes, Lorem Ipsum</p></div>
<div class="abs" style="left:795px;top:3697px;width:346px;height:216px;background:#fff;padding:44px 28px 0"><div class="abs" style="left:28px;top:-20px;width:44px;height:44px;border-radius:50%;background:var(--blue);color:#fff;font-size:30px;font-weight:700;text-align:center;line-height:52px">“</div><p style="font-size:13.5px;font-weight:500;line-height:1.9">Lorem ipsum dolor sit amet, conteuer adipiscing elit, sed diam nonummy nibh euismod tincidunt ut laoreet dolore magna aliquam erat volutpat.</p><p style="font-size:11.5px;color:var(--muted);margin-top:26px">Dana Reyes, Lorem Ipsum</p></div>
<div class="abs" style="left:574px;top:3940px;display:flex;gap:16px;align-items:center"><span style="width:6px;height:6px;border-radius:50%;background:var(--blue-soft)"></span><span style="width:8px;height:8px;border-radius:50%;background:var(--blue)"></span><span style="width:6px;height:6px;border-radius:50%;background:var(--blue-soft)"></span></div>

<!-- Blog -->
<h2 class="abs center-title" style="top:4082px"><span class="brand" style="font-weight:600">From</span> <span class="brand">CoverLantern</span> Blog</h2>
<article class="abs" style="left:61px;top:4147px;width:346px;height:380px;background:#fff;box-shadow:0 6px 20px rgba(0,40,90,.08)"><div role="img" aria-label="Photo of a family walking together outdoors in autumn" style="height:236px;background:linear-gradient(150deg,#efe7d6,#b99a6e 60%,#6f5a3d)"></div><div style="padding:18px 26px"><p style="font-size:11px;color:var(--muted)">April 5, 2022</p><p style="font-size:13.5px;font-weight:500;line-height:1.7;margin-top:10px">Lorem ipsum dolor sit amet, conter adipiscing elit, sed diam.</p><p style="font-size:11px;font-weight:600;color:var(--blue);margin-top:18px">READ MORE</p></div></article>
<article class="abs" style="left:428px;top:4147px;width:345px;height:380px;background:#fff;box-shadow:0 6px 20px rgba(0,40,90,.08)"><div role="img" aria-label="Photo of a doctor's hands sheltering a small paper family" style="height:236px;background:linear-gradient(160deg,#f4f5f7,#dcdfe4 60%,#b9bfc8)"></div><div style="padding:18px 26px"><p style="font-size:11px;color:var(--muted)">April 5, 2022</p><p style="font-size:13.5px;font-weight:500;line-height:1.7;margin-top:10px">Lorem ipsum dolor sit amet, conter adipiscing elit, sed diam.</p><p style="font-size:11px;font-weight:600;color:var(--blue);margin-top:18px;text-decoration:underline">READ MORE</p></div></article>
<article class="abs" style="left:795px;top:4147px;width:346px;height:380px;background:#fff;box-shadow:0 6px 20px rgba(0,40,90,.08)"><div role="img" aria-label="Photo of grandparents laughing with their grandchildren" style="height:236px;background:linear-gradient(150deg,#e8ddd3,#c59b86 55%,#7d5a4a)"></div><div style="padding:18px 26px"><p style="font-size:11px;color:var(--muted)">April 5, 2022</p><p style="font-size:13.5px;font-weight:500;line-height:1.7;margin-top:10px">Lorem ipsum dolor sit amet, conter adipiscing elit, sed diam.</p><p style="font-size:11px;font-weight:600;color:var(--blue);margin-top:18px">READ MORE</p></div></article>

<!-- Quote CTA -->
<h2 class="abs center-title" style="top:4632px">Get Your <span style="color:var(--teal);font-weight:700">FREE</span> Quote Now</h2>
<p class="abs" style="left:0;width:1200px;text-align:center;top:4688px;font-size:13.5px;color:var(--muted)">See your CoverLantern Free-Quote in seconds.</p>
<a class="abs btn" style="left:522px;top:4733px;height:40px;width:156px;justify-content:center;padding:0">FREE QUOTES <svg viewBox="0 0 18 10"><path d="M0 5h16M12 1l4 4-4 4" stroke="#fff" stroke-width="1.6" fill="none"/></svg></a>

<!-- Footer -->
<footer class="abs footer">
  <div class="abs" style="left:60px;top:72px;font-size:32px;font-weight:400;color:#fff">CoverLantern</div>
  <div class="abs" style="left:72px;top:142px;display:flex;gap:10px">
    <span style="width:32px;height:32px;border-radius:50%;border:2px solid var(--lime)"></span>
    <span style="width:32px;height:32px;border-radius:50%;border:2px solid var(--lime)"></span>
    <span style="width:32px;height:32px;border-radius:50%;border:2px solid var(--lime)"></span>
    <span style="width:32px;height:32px;border-radius:50%;border:2px solid var(--lime)"></span>
  </div>
  <div class="abs" style="left:300px;top:64px"><h4>Quick Links</h4><ul><li>Free Quote</li><li>No Exam</li><li>Articles</li><li>FAQ's</li><li>About</li><li>Contact</li></ul></div>
  <div class="abs" style="left:459px;top:64px"><h4>Our Products</h4><ul><li>10 Year Level Team</li><li>15 Year Level Team</li><li>20 Year Level Team</li><li>30 Year Level Team</li><li>Lifetime Coverage</li></ul></div>
  <div class="abs" style="left:645px;top:64px"><h4>Tools</h4><ul><li>Quote Comparison</li><li>Secure Client Portal</li><li>Privacy Policy</li></ul></div>
  <div class="abs" style="left:831px;top:64px;width:310px"><h4>Contact Us</h4><ul class="contact-list"><li>Phone: <b>1-888-555-0142</b></li><li>Mail: <b style="text-decoration:underline">info@CoverLantern.com</b></li><li>Monday - Friday: <strong>9:00 AM - 8:00 PM</strong></li><li style="line-height:20px">Address: <strong>4410 HARBOR POINT DRIVE, SUITE 120,<br>LAKE MARY, FL 32746</strong></li></ul></div>

  <div class="abs" style="left:60px;top:287px;width:1080px;height:88px;background:var(--navy);display:flex;align-items:center">
    <span style="margin-left:75px;font-size:28px;font-weight:500">Subscribe To Our Newsletter</span>
    <svg style="margin-left:112px" width="30" height="24" viewBox="0 0 30 24"><path d="M2 10L28 2 22 22 14 15z M14 15l-2 7" fill="none" stroke="#59FF00" stroke-width="1.6"/></svg>
    <div style="margin-left:6px;width:260px;height:38px;border:1px solid #7BADD7;border-radius:19px 0 0 19px;border-right:none;display:flex;align-items:center;padding-left:16px;font-size:11px">Email Address</div>
    <div style="width:114px;height:38px;background:var(--lime);border-radius:0 19px 19px 0;color:var(--navy);font-size:11.5px;font-weight:600;display:flex;align-items:center;justify-content:center">SUBSCRIBE</div>
  </div>
  <p class="abs" style="left:0;width:1200px;text-align:center;top:396px;font-size:11px">© CoverLantern - 2022. All Rights Reserved.</p>
</footer>

</body>
</html>
```